Black Car Limousine transportation business in Naples Florida

Always stand for my reliability and RNT stands for Rest, N and T are the first initials of my children's names. It should show professionalism and a dedication to customer service. We keep our clients identities private. Show our professionalism. We are Black car Black tie company. We service transportation on a reserve basis to and from residents, airports, casinos, hotels,

Target Market(s)

It is a Private car service. High end clients. Businesses, Celebrity and athletes. Service to airports, hotels, special events.

Industry/Entity Type

Business

Contact Information for Business Card

A pearl metallic or Luster card. Standard business card size. Would like the name, Company email, show we take credit cards and phone number. Currently I don't have a website but will like to add later.

Logo Text

STEADFAST RNT TRANSPORTATION

Font styles to use
Serif

Colors
eaeaea
000000

Requirements
Must have
• Must have Company email, show we take credit cards and phone number. Currently I don't have a website but will like to add later.
Nice to have
• Would like to stay with a black and white theme. Open to some color trim.
Should not have
• Open to suggestions

```html
<!DOCTYPE html>
<html lang="en">
<head>
<meta charset="utf-8">
<title>Steadfast RNT Transportation – Business Card</title>
<link href="https://fonts.googleapis.com/css2?family=Cormorant+Garamond:wght@400;500&family=Lora:wght@400;700&display=swap" rel="stylesheet">
<style>
  :root {
    --backdrop: #a7a8aa;
    --card: #070303;
    --ink: #eaeaea;
    --ink-soft: #d2d2d2;
    --shade-top: #141414;
    --shade-bottom: #090606;
  }
  html, body {
    margin: 0;
    padding: 0;
    width: 1200px;
    height: 545px;
    overflow: hidden;
    background: var(--backdrop);
  }
  .canvas {
    position: relative;
    width: 1200px;
    height: 545px;
  }
  .card {
    position: absolute;
    top: 136px;
    width: 477px;
    height: 274px;
    background: var(--card);
    overflow: hidden;
  }
  .card--front { left: 108px; }
  .card--back { left: 615px; }

  .brand {
    position: absolute;
    left: 68px;
    top: 103px;
    height: 60px;
    display: flex;
    align-items: center;
    gap: 21px;
  }
  .brand__mark {
    width: 60px;
    height: 60px;
    border: 1px solid var(--ink);
    border-radius: 50%;
    box-sizing: border-box;
    display: flex;
    align-items: center;
    justify-content: center;
    font-family: "Cormorant Garamond", serif;
    font-weight: 500;
    font-size: 20px;
    letter-spacing: 0.5px;
    color: var(--ink);
  }
  .brand__name {
    font-family: "Cormorant Garamond", serif;
    font-weight: 500;
    font-size: 17px;
    letter-spacing: 1.3px;
    color: var(--ink);
    white-space: nowrap;
  }
  .vehicle {
    position: absolute;
    left: 277px;
    top: 218px;
    width: 191px;
    height: 56px;
    border-radius: 46px 34px 0 0;
    background: linear-gradient(180deg, var(--shade-top) 0%, var(--shade-bottom) 100%);
  }

  .contact {
    position: absolute;
    left: 49px;
    top: 140px;
    font-family: "Lora", serif;
    font-size: 9px;
    line-height: 14.5px;
    color: var(--ink-soft);
  }
  .contact p { margin: 0; }
  .contact__title {
    font-weight: 700;
    font-size: 9.5px;
    color: var(--ink);
  }
  .contact__group + .contact__group { margin-top: 14.5px; }
</style>
</head>
<body>
  <main class="canvas">
    <section class="card card--front" aria-label="Card front">
      <div class="brand">
        <div class="brand__mark">RNT</div>
        <div class="brand__name">STEADFAST RNT TRANSPORTATION</div>
      </div>
      <div class="vehicle" role="img" aria-label="Faint outline silhouette of a luxury SUV in the lower right corner"></div>
    </section>

    <section class="card card--back" aria-label="Card back">
      <div class="contact">
        <div class="contact__group">
          <p class="contact__title">Darius Reed, Owner</p>
          <p>Phone (239) 555-0148 · Naples, Florida</p>
          <p>info@steadfastrnt.com</p>
        </div>
        <div class="contact__group">
          <p>All major credit cards accepted</p>
          <p>Private service by reservation</p>
        </div>
      </div>
    </section>
  </main>
</body>
</html>
```